Meridian Handsets business card design

I would like to see some designs for a business card for Meridian Handsets. I would like the business card to be double sided. It will need to have a similar colour / look and feel to our website www.meridianhandsets.com.au I have also attached our latest flyer. Final designs to be handed over in Photoshop format so that I can edit the business card when needed please.

Industry/Entity Type

Business

Contact Information for Business Card

Gavin Thornley
sales@meridianhandsets.com.au
Business Development Manager
ph: (08) 6197 5821
www.meridianhandsets.com.au

Font styles to use
Serif
Sans Serif

Requirements
Must have
• If you could please utilise our colour scheme as seen on our website and the attached flyer.
• I would also like the final design to be in a Photoshop format so that I can edit it when needed please.

```html
<!DOCTYPE html>
<html lang="en">
<head>
<meta charset="utf-8">
<title>Meridian Handsets – Business Card</title>
<link href="https://fonts.googleapis.com/css2?family=Montserrat:wght@600;700&family=Open+Sans:wght@400;600&display=swap" rel="stylesheet">
<style>
  :root {
    --page-bg: #3a3a3c;
    --card-bg: #1b1c1e;
    --brand-blue: #1a7fc1;
    --text-white: #ffffff;
    --text-soft: #e8e8e8;
    --divider: #d9d9d9;
  }
  * { margin: 0; padding: 0; box-sizing: border-box; }
  html, body {
    width: 1200px; height: 1189px; overflow: hidden;
    background: var(--page-bg);
  }
  .sheet {
    width: 1200px; height: 1189px;
    display: flex; flex-direction: column;
    align-items: center; justify-content: center; gap: 46px;
  }
  .card {
    position: relative;
    width: 860px; height: 524px;
    background: var(--card-bg);
    border-radius: 28px;
    box-shadow: 0 18px 40px rgba(0,0,0,0.45);
    overflow: hidden;
  }
  .brand-name {
    font-family: "Montserrat", sans-serif;
    font-weight: 700;
    font-size: 68px;
    color: var(--text-white);
    letter-spacing: 1px;
    white-space: nowrap;
    line-height: 1.1;
  }

  /* Front */
  .brand-block {
    position: absolute; left: 0; right: 0; top: 190px;
    display: flex; justify-content: center;
  }
  .brand-block__inner {
    display: flex; flex-direction: column; align-items: flex-end;
  }
  .web-line {
    margin-top: 14px; margin-right: 20px;
    font-family: "Open Sans", sans-serif; font-size: 19px;
    color: var(--text-soft);
  }

  /* Back */
  .card--back .brand-name {
    position: absolute; left: 0; right: 0; top: 120px;
    text-align: center;
  }
  .person {
    position: absolute; right: 452px; top: 318px;
    text-align: right;
    font-family: "Open Sans", sans-serif; color: var(--text-white);
  }
  .person__name {
    font-family: "Montserrat", sans-serif; font-weight: 700;
    font-size: 34px; color: var(--brand-blue); line-height: 1.1;
  }
  .person__title { font-size: 22px; line-height: 1.3; }
  .person__address { margin-top: 16px; font-size: 22px; line-height: 1.35; }
  .divider {
    position: absolute; left: 428px; top: 310px;
    width: 2px; height: 150px; background: var(--divider);
  }
  .contact {
    position: absolute; left: 456px; top: 328px;
    list-style: none;
    font-family: "Open Sans", sans-serif; font-size: 21px; color: var(--text-white);
  }
  .contact__item {
    display: flex; align-items: center; gap: 12px; height: 40px;
  }
  .contact__icon {
    width: 30px; height: 30px; border-radius: 5px;
    background: var(--brand-blue);
    display: flex; align-items: center; justify-content: center;
    flex: none;
  }
</style>
</head>
<body>
<main class="sheet">
  <section class="card card--front" aria-label="Card front">
    <div class="brand-block">
      <div class="brand-block__inner">
        <p class="brand-name">Meridian Handsets</p>
        <p class="web-line">www.meridianhandsets.com.au</p>
      </div>
    </div>
  </section>

  <section class="card card--back" aria-label="Card back">
    <p class="brand-name">Meridian Handsets</p>

    <div class="person">
      <p class="person__name">Gavin Thornley</p>
      <p class="person__title">Business Development Manager</p>
      <p class="person__address">Fourth Street, Maylands<br>Western Australia 6051 Australia</p>
    </div>

    <span class="divider"></span>

    <ul class="contact">
      <li class="contact__item">
        <span class="contact__icon">
          <svg width="18" height="18" viewBox="0 0 24 24"><path fill="#fff" d="M6.6 10.8a15.1 15.1 0 0 0 6.6 6.6l2.2-2.2c.3-.3.7-.4 1-.2 1.1.4 2.3.6 3.6.6.6 0 1 .4 1 1V20c0 .6-.4 1-1 1A17 17 0 0 1 3 4c0-.6.4-1 1-1h3.5c.6 0 1 .4 1 1 0 1.3.2 2.5.6 3.6.1.3 0 .7-.2 1z"/></svg>
        </span>(08) 6197 5821
      </li>
      <li class="contact__item">
        <span class="contact__icon">
          <svg width="18" height="18" viewBox="0 0 24 24" fill="none" stroke="#fff" stroke-width="2"><rect x="3" y="6" width="18" height="12" rx="1"/><path d="M3 7l9 6 9-6"/></svg>
        </span>sales@meridianhandsets.com.au
      </li>
      <li class="contact__item">
        <span class="contact__icon">
          <svg width="18" height="18" viewBox="0 0 24 24" fill="none" stroke="#fff" stroke-width="1.8"><circle cx="12" cy="12" r="9"/><ellipse cx="12" cy="12" rx="4" ry="9"/><path d="M3 12h18M5 7h14M5 17h14"/></svg>
        </span>www.meridianhandsets.com.au
      </li>
    </ul>
  </section>
</main>
</body>
</html>
```